Corvanta Stationery Design

We need design for our stationary, including:
1) Letterhead
- A4/Letter size in landscape and portrait letterhead
- The letterhead must be in a word file, and the address should be editable using the Felixti or Perpetua Titling TTF
- The output file should be in .docx and in .ai.
2) Business card
- The business card will be printed in white paper and single face only, so there should be nothing on the reverse side.
3) Envelope (sizes A4, Letter, and small document)
Please refer to the picture showing some samples of stationary with designs that would fulfill our wish.
We're including the logo in .AI.
Thanks
Target Market(s)
High end investors
Industry/Entity Type
Landscape
Look and feel
Each slider illustrates characteristics of the customer's brand and the style your logo design should communicate.

```html
<!DOCTYPE html>
<html lang="en">
<head>
<meta charset="utf-8">
<title>Corvanta Capital Partners – Business Card</title>
<link rel="stylesheet" href="https://fonts.googleapis.com/css2?family=Cinzel:wght@400;700&display=swap">
<style>
  :root {
    --paper: #ffffff;
    --brand-blue: #0099bf;
    --ink-dark: #333333;
    --text-light: #ffffff;
  }
  html, body {
    margin: 0;
    padding: 0;
    width: 1200px;
    height: 804px;
    overflow: hidden;
    background: var(--paper);
  }
  .card {
    position: relative;
    width: 1200px;
    height: 804px;
    background: var(--paper);
    overflow: hidden;
  }
  .wordmark {
    position: absolute;
    top: 70px;
    left: 680px;
    width: 445px;
    color: var(--ink-dark);
    font-family: "Cinzel", serif;
    font-weight: 400;
    text-align: center;
  }
  .wordmark-name {
    display: block;
    font-size: 72px;
    line-height: 1;
    letter-spacing: 3px;
    text-transform: uppercase;
  }
  .wordmark-tagline {
    display: block;
    margin-top: 12px;
    font-size: 24px;
    letter-spacing: 9px;
    text-transform: uppercase;
  }
  .contact-band {
    position: absolute;
    left: 0;
    top: 0;
    width: 1200px;
    height: 804px;
  }
  .contact-band path {
    fill: var(--brand-blue);
  }
  .contact-list {
    position: absolute;
    left: 47px;
    top: 503px;
    margin: 0;
    padding: 0;
    list-style: none;
    color: var(--text-light);
    font-family: "Cinzel", serif;
    font-weight: 700;
    font-size: 35px;
    line-height: 44.6px;
    letter-spacing: 0.5px;
  }
</style>
</head>
<body>
  <div class="card">
    <div class="wordmark">
      <span class="wordmark-name">Corvanta</span>
      <span class="wordmark-tagline">Capital Partners</span>
    </div>

    <svg class="contact-band" viewBox="0 0 1200 804" aria-hidden="true">
      <path d="M0 463 Q614 416 1200 469 L1200 804 L0 804 Z"/>
    </svg>

    <ul class="contact-list">
      <li>This is all our contact information</li>
      <li>Our address</li>
      <li>Our phone number</li>
      <li>Our email</li>
      <li>Website</li>
      <li>Any other information</li>
    </ul>
  </div>
</body>
</html>
```